Brantley Advisory Group provides support for renewable energy projects to utilities and suppliers

I need a professional looking business card that is both simple and elegant and unique. My clients are mostly large organizations not individuals. I am a consultant with my own company that is small but would like to give clients the impression I am larger. Smart grid, fiber optics, software, field hardware, distribution automation, substation automation, operations, energy storage/batteries, microgrids, customer service, strategy/roadmaps, conservation, Automated Metering Infrastruture (AMI or smart meters) are all areas of focus.

Target Market(s)

Utilities, suppliers, governmental agencies involved in energy. All types of energy especially natural gas and electrical. Especially renewable energy or green projects.

Contact Information for Business Card

Name - Mark Brantley Cell Phone - 425.318.2746 Email - mbrantley@brantleyag-example.com
Company - Brantley Advisory Group (logo) Title - Principal

Font styles to use
Serif
Sans Serif

Colors

Designer to choose colors to be used in the design.

Requirements
Must have
• Simple and professional and powerful.
• Unique/creative design.
Nice to have
• Utilize color scheme to accent logo colors. Maybe some geometric pattern on edge of card with color.
Should not have
• Busy, complicated, traditional

```html
<!DOCTYPE html>
<html lang="en">
<head>
<meta charset="utf-8">
<title>Brantley Advisory Group – Business Card</title>
<link rel="stylesheet" href="https://fonts.googleapis.com/css2?family=Montserrat:wght@300;400;600;700&display=swap">
<style>
  :root {
    --brand-blue: #0c12a0;
    --brand-green: #5e8a3c;
    --ink-grey: #555a60;
    --paper: #ffffff;
    --backdrop: #e6e7ea;
  }
  * { margin: 0; padding: 0; box-sizing: border-box; }
  html, body {
    width: 1200px; height: 912px; overflow: hidden;
    background: var(--backdrop);
    font-family: "Montserrat", sans-serif;
  }
  .stage {
    width: 1200px; height: 912px;
    display: flex; align-items: center; justify-content: center; gap: 44px;
  }
  .card {
    position: relative;
    width: 540px; height: 310px;
    overflow: hidden;
    box-shadow: 0 6px 18px rgba(0,0,0,0.18);
  }

  /* Front */
  .card-front {
    background: var(--brand-blue);
    display: flex; align-items: center; justify-content: center;
  }
  .brand {
    display: flex; align-items: center; gap: 14px;
  }
  .brand-square {
    width: 34px; height: 34px;
    border: 3px solid currentColor; border-radius: 5px;
    flex: none;
  }
  .brand-name {
    font-weight: 700; font-size: 27px; letter-spacing: 0.5px; line-height: 1.1;
  }
  .card-front .brand { color: var(--paper); }

  /* Back */
  .card-back { background: var(--paper); }
  .card-back .brand {
    position: absolute; left: 36px; top: 46px;
    color: var(--brand-blue);
  }
  .card-back .brand-name { font-size: 22px; }
  .card-back .brand-square { width: 28px; height: 28px; }

  .side-tab {
    position: absolute; right: 0; top: 104px;
    width: 18px; height: 38px;
    background: var(--brand-blue);
  }
  .person {
    position: absolute; right: 36px; top: 100px;
    text-align: right;
  }
  .person-name {
    font-weight: 700; font-size: 26px; color: var(--brand-blue); line-height: 1;
  }
  .person-name .surname { color: var(--brand-green); }
  .person-title {
    font-weight: 400; font-size: 12px; color: var(--ink-grey);
    margin-top: 4px; letter-spacing: 0.5px;
  }

  .contact-band {
    position: absolute; left: 36%; top: 158px; right: 0; bottom: 0;
    background: var(--brand-blue);
    border-top-left-radius: 12px;
  }
  .contact-list {
    position: absolute; right: 22px; top: 16px;
    list-style: none; color: var(--paper);
    font-size: 12px; font-weight: 400; letter-spacing: 0.2px;
  }
  .contact-list li {
    display: flex; align-items: center; justify-content: flex-end; gap: 8px;
    margin-bottom: 7px;
  }
  .contact-icon { width: 14px; height: 14px; flex: none; }
</style>
</head>
<body>
<main class="stage">
  <section class="card card-front" aria-label="Card front">
    <div class="brand">
      <span class="brand-square"></span>
      <span class="brand-name">Brantley<br>Advisory Group</span>
    </div>
  </section>

  <section class="card card-back" aria-label="Card back">
    <div class="brand">
      <span class="brand-square"></span>
      <span class="brand-name">Brantley<br>Advisory Group</span>
    </div>

    <span class="side-tab"></span>
    <div class="person">
      <p class="person-name">Mark <span class="surname">Brantley</span></p>
      <p class="person-title">Principal</p>
    </div>

    <div class="contact-band">
      <ul class="contact-list">
        <li>425.318.2746
          <svg class="contact-icon" viewBox="0 0 14 14" fill="none" stroke="#fff" stroke-width="1.2">
            <rect x="0.6" y="0.6" width="12.8" height="12.8" rx="3"/>
            <path d="M4.3 3.5l1.4 0.2 0.5 1.6-0.9 0.8c0.5 1 1.1 1.6 2.1 2.1l0.8-0.9 1.6 0.5 0.2 1.4c-2.9 0.6-6.3-2.8-5.7-5.7z"/>
          </svg>
        </li>
        <li>mbrantley@brantleyag-example.com
          <svg class="contact-icon" viewBox="0 0 14 14" fill="none" stroke="#fff" stroke-width="1.2">
            <rect x="0.6" y="0.6" width="12.8" height="12.8" rx="3"/>
            <rect x="3" y="4" width="8" height="6"/>
            <path d="M3 4l4 3.2 4-3.2"/>
          </svg>
        </li>
        <li>www.brantleyag-example.com
          <svg class="contact-icon" viewBox="0 0 14 14" fill="none" stroke="#fff" stroke-width="1.2">
            <circle cx="7" cy="7" r="6.2"/>
            <ellipse cx="7" cy="7" rx="2.6" ry="6.2"/>
            <path d="M1 7h12"/>
          </svg>
        </li>
      </ul>
    </div>
  </section>
</main>
</body>
</html>
```